Awesome new dental practice requires a New Letterhead design

We would like a new letterhead design to align with our new business branding & business cards. I have uploaded all the logos & current business card details that can be used. The new website can be viewed here https://lumaveo.com.au

Other useful details: Font Poppins
Colour Palettes:
Dark Pink #c45389
Light Pink: #e83e8c
Black

Please let me know if you have any questions or require anything else.

Industry/Entity Type

Dental

Font styles to use
Other font styles liked:
• Poppins

```html
<!DOCTYPE html>
<html lang="en">
<head>
<meta charset="utf-8">
<title>Lumaveo Letterhead</title>
<link href="https://fonts.googleapis.com/css2?family=Open+Sans:wght@400&family=Poppins:wght@400;500&display=swap" rel="stylesheet">
<style>
  :root {
    --backdrop: #e2e2e2;
    --paper: #f8f8f8;
    --ink: #111111;
    --body-text: #4a4a4a;
    --contact-text: #474747;
    --pink-dark: #c45389;
    --pink-light: #e83e8c;
    --signature-tone: #dcdcdc;
  }
  * { box-sizing: border-box; margin: 0; padding: 0; }
  html, body {
    width: 1153px;
    height: 1200px;
    overflow: hidden;
    background: var(--backdrop);
  }
  .letterhead {
    position: absolute;
    left: 168px;
    top: 30px;
    width: 817px;
    height: 1140px;
    background: var(--paper);
    box-shadow: 0 6px 24px rgba(0, 0, 0, 0.12);
  }
  .brand-name {
    position: absolute;
    left: 87px;
    top: 100px;
    font-family: "Poppins", sans-serif;
    font-weight: 500;
    font-size: 42px;
    line-height: 1;
    letter-spacing: -0.5px;
    color: var(--ink);
  }
  .contact-list {
    position: absolute;
    left: 519px;
    top: 72px;
    list-style: none;
    font-family: "Poppins", sans-serif;
    font-size: 15px;
    color: var(--contact-text);
  }
  .contact-item {
    display: flex;
    align-items: flex-start;
    line-height: 19px;
    margin-bottom: 3px;
  }
  .contact-item.address { margin-bottom: 9px; }
  .contact-icon {
    flex: none;
    width: 13px;
    height: 13px;
    margin: 3px 3px 0 0;
    fill: var(--pink-light);
  }
  .letter-body {
    position: absolute;
    left: 73px;
    top: 253px;
    width: 670px;
    font-family: "Open Sans", sans-serif;
    font-size: 14.4px;
    line-height: 22px;
    letter-spacing: -0.05px;
    color: var(--body-text);
  }
  .letter-body p {
    text-align: justify;
    margin-bottom: 22px;
  }
  .letter-body .salutation,
  .letter-body .closing { text-align: left; }
  .signature-area {
    width: 94px;
    height: 89px;
    margin: 4px 0 0 2px;
    background: var(--signature-tone);
  }
</style>
</head>
<body>
  <main class="letterhead">
    <header>
      <div class="brand-name">Lumaveo</div>
      <ul class="contact-list">
        <li class="contact-item address">
          <svg class="contact-icon" viewBox="0 0 12 16" aria-hidden="true"><path d="M6 0a6 6 0 0 0-6 6c0 4.5 6 10 6 10s6-5.5 6-10a6 6 0 0 0-6-6zm0 8.3A2.3 2.3 0 1 1 6 3.7a2.3 2.3 0 0 1 0 4.6z"/></svg>
          <span>Suite 7, 42 Harbour Parade<br>Seabrook WA</span>
        </li>
        <li class="contact-item">
          <svg class="contact-icon" viewBox="0 0 16 16" aria-hidden="true"><path d="M3.6 1.2l2.2 2.7c.4.5.3 1.1-.1 1.5L4.6 6.5c.9 2 2.6 3.8 4.8 4.9l1.1-1.1c.4-.4 1.1-.5 1.5-.1l2.7 2.2c.5.4.5 1.1.1 1.5l-1.4 1.4C11 17 .1 6 1.8 3.7L3.2 2.2c.1-.3.3-.8.4-1z"/></svg>
          <span>(08) 9400 2187</span>
        </li>
        <li class="contact-item">
          <svg class="contact-icon" viewBox="0 0 16 12" aria-hidden="true"><path d="M0 1.5V0h16v1.5L8 6.5 0 1.5zm0 1.8l8 5 8-5V12H0V3.3z"/></svg>
          <span>hello@lumaveo.com</span>
        </li>
        <li class="contact-item">
          <svg class="contact-icon" viewBox="0 0 16 16" aria-hidden="true"><circle cx="8" cy="8" r="8"/><path d="M4 3.5c1.5.4 2.5 1.6 2 3-.6 1.4-2.4.9-2.4 2.6 0 1.3 1.2 1.7 1.2 3.6M10.5 2.8c-.6 1.4.3 2.3 1.7 2.5M13 9.5c-1.4-.3-2.6.6-2.4 2 .1 1 .6 1.6.4 2.6" fill="none" stroke="#f8f8f8" stroke-width="1.3"/></svg>
          <span>www.lumaveo.com.au</span>
        </li>
      </ul>
    </header>

    <section class="letter-body">
      <p class="salutation">Dear customer,</p>
      <p>Lorem ipsum dolor sit amet, consectetur adipisicing elit, sed do eiusmod tempor incididunt ut labore et dolore magna aliqua. Ut enim ad minim veniam, quis nostrud exercitation ullamco laboris nisi ut aliquip ex ea commodo consequat. Duis aute irure dolor in reprehenderit in voluptate velit esse cillum dolore eu fugiat nulla pariatur. Excepteur sint occaecat cupidatat non proident, sunt in culpa qui officia deserunt mollit anim id est laborum.</p>
      <p>Lorem ipsum dolor sit amet, consectetur adipisicing elit, sed do eiusmod tempor incididunt ut labore et dolore magna aliqua. Ut enim ad minim veniam, quis nostrud exercitation ullamco laboris nisi ut aliquip ex ea commodo consequat. Duis aute irure dolor in reprehenderit in voluptate velit esse cillum dolore eu fugiat nulla pariatur. Excepteur sint occaecat cupidatat non proident, sunt in culpa qui officia deserunt mollit anim id est laborum.</p>
      <p>Lorem ipsum dolor sit amet, consectetur adipisicing elit, sed do eiusmod tempor incididunt ut labore et dolore magna aliqua. Ut enim ad minim veniam, quis nostrud exercitation ullamco laboris nisi ut aliquip ex ea commodo consequat. Duis aute irure dolor in reprehenderit in voluptate velit esse cillum dolore eu fugiat nulla pariatur. Excepteur sint occaecat cupidatat non proident, sunt in culpa qui officia deserunt mollit anim id est laborum.</p>
      <p>Lorem ipsum dolor sit amet, consectetur adipisicing elit, sed do eiusmod tempor incididunt ut labore et dolore magna aliqua. Ut enim ad minim veniam, quis nostrud exercitation ullamco laboris nisi ut aliquip ex ea commodo consequat. Duis aute irure dolor in reprehenderit.</p>
      <p class="closing">Yours Sincerely,</p>
      <div class="signature-area" role="img" aria-label="Handwritten signature of the sender"></div>
    </section>
  </main>
</body>
</html>
```